Case Study - template Visual Design

We need to convert our current case study document into something more cosmetically pleasing and easy to read. (primary goal). We also want to make sure the design is reusable for future case studies as well.
Current case study content is uploaded for reference.
Company is Zentho.ai
Target Market(s)
Mid to large Enterprise
Industry/Entity Type
Iot
Font styles to use
Sans Serif
Colors
Designer to choose colors to be used in the design.

```html
<!DOCTYPE html>
<html lang="en">
<head>
<meta charset="utf-8">
<title>Zentho.ai Case Study Template</title>
<link rel="stylesheet" href="https://fonts.googleapis.com/css2?family=Oswald:wght@500&family=Roboto:ital,wght@0,300;0,400;0,500;0,700;1,400&family=Roboto+Condensed:ital,wght@0,400;1,400&display=swap">
<style>
  :root {
    --stage: #c8c8c8;
    --green: #52cc87;
    --purple: #6a4ce0;
    --paper-light: #f7f7fa;
    --ink: #111114;
    --body-gray: #7a7a80;
    --label: #1e1e22;
    --tile: #ffffff;
  }
  * { box-sizing: border-box; margin: 0; padding: 0; }
  html, body { width: 1200px; height: 656px; overflow: hidden; }
  body {
    background: var(--stage);
    font-family: "Roboto", Arial, sans-serif;
    position: relative;
  }
  .page {
    position: absolute;
    top: 79px;
    width: 334px;
    height: 473px;
    overflow: hidden;
    box-shadow: 0 2px 6px rgba(0,0,0,.22);
  }
  .page-label {
    position: absolute;
    top: 574px;
    width: 334px;
    text-align: center;
    font-size: 10px;
    font-weight: 500;
    letter-spacing: 1px;
    color: var(--label);
  }
  .front, .front-label { left: 69px; }
  .inner, .inner-label { left: 434px; }
  .back, .back-label { left: 798px; }

  /* Front cover */
  .front { background: linear-gradient(160deg, var(--paper-light), #dcdce4); }
  .front .shapes { position: absolute; inset: 0; }
  .front .brand {
    position: absolute; left: 190px; top: 128px;
    font-size: 36px; font-weight: 700; color: var(--ink); letter-spacing: -0.5px;
  }
  .cover-title {
    position: absolute; left: 14px; top: 235px; width: 206px;
    text-align: center;
    font-family: "Oswald", "Arial Narrow", sans-serif;
    font-weight: 500; font-size: 17.5px; line-height: 20.5px;
    color: #fff;
  }
  .industry-grid {
    position: absolute; left: 25px; top: 326px;
    display: grid; grid-template-columns: repeat(3, 60px); gap: 4px;
  }
  .industry-tile {
    width: 60px; height: 60px; border-radius: 6px;
    background: var(--tile);
    display: flex; align-items: center; justify-content: center;
  }
  .industry-tile span {
    width: 28px; height: 28px; border-radius: 4px;
    background: linear-gradient(135deg, #8d74ee, var(--purple));
    opacity: .85;
  }

  /* Inner page */
  .inner { background: linear-gradient(180deg, var(--paper-light), #e6e6ec); }
  .inner .brand {
    position: absolute; left: 30px; top: 40px;
    display: flex; align-items: center; gap: 6px;
    font-size: 19px; font-weight: 700; color: var(--ink);
  }
  .brand-mark { width: 14px; height: 14px; background: var(--green); }
  .article { position: absolute; left: 30px; top: 92px; width: 274px; }
  .article h1 {
    font-size: 11.4px; font-weight: 700; line-height: 13.5px;
    color: var(--ink); margin-bottom: 3px;
  }
  .article p {
    font-size: 9.2px; line-height: 11.3px; font-weight: 300;
    color: var(--body-gray); text-align: justify; margin-bottom: 11px;
  }
  .article strong { font-weight: 400; color: var(--ink); }
  .article .pull-quote { color: var(--ink); font-weight: 400; }
  .page-footer {
    position: absolute; left: 30px; top: 437px; width: 274px;
    border-top: 1.5px solid var(--purple);
    display: flex; justify-content: space-between;
    padding-top: 4px;
    font-size: 4.8px; color: #555;
  }
  .page-footer .site { color: var(--purple); font-weight: 700; letter-spacing: .3px; }
  .page-footer .num { color: var(--green); font-weight: 700; margin-left: 3px; }

  /* Back cover */
  .back { background: linear-gradient(150deg, #f4f4f8, #ececf2); }
  .back .bands { position: absolute; inset: 0; }
  .contact {
    position: absolute; left: 0; top: 144px; width: 334px; text-align: center;
  }
  .contact .brand {
    font-size: 34px; font-weight: 700; color: var(--ink); margin-bottom: 40px;
  }
  .contact h2 { font-size: 16.5px; font-weight: 700; color: var(--ink); margin-bottom: 9px; }
  .contact .about {
    width: 176px; margin: 0 auto 10px;
    font-family: "Roboto Condensed", "Arial Narrow", sans-serif;
    font-size: 7px; line-height: 9.4px; color: #444;
  }
  .contact .details {
    font-family: "Roboto Condensed", "Arial Narrow", sans-serif;
    font-size: 9px; color: var(--ink); margin-bottom: 13px;
  }
  .contact .copyright {
    font-family: "Roboto Condensed", "Arial Narrow", sans-serif;
    font-size: 6px; font-style: italic; color: #666;
  }
</style>
</head>
<body>

  <section class="page front">
    <svg class="shapes" width="334" height="473" viewBox="0 0 334 473" aria-hidden="true">
      <polygon points="0,0 189,0 95,106" fill="var(--purple)"/>
      <polygon points="0,0 334,374 334,473 0,473" fill="var(--green)"/>
    </svg>
    <div class="brand">Zentho</div>
    <h1 class="cover-title">HOW ZENTHO<br>DRIVES ADOPTION OF<br>PREDICTIVE MAINTENANCE<br>WITH MACHINE LEARNING</h1>
    <div class="industry-grid">
      <div class="industry-tile" role="img" aria-label="Manufacturing gripper icon"><span></span></div>
      <div class="industry-tile" role="img" aria-label="Construction and robotics icon"><span></span></div>
      <div class="industry-tile" role="img" aria-label="Industrial printing icon"><span></span></div>
      <div class="industry-tile" role="img" aria-label="Oil and gas rig icon"><span></span></div>
      <div class="industry-tile" role="img" aria-label="Healthcare stethoscope icon"><span></span></div>
      <div class="industry-tile" role="img" aria-label="Defense jet icon"><span></span></div>
    </div>
  </section>
  <div class="page-label front-label">FRONT</div>

  <section class="page inner">
    <div class="brand"><span class="brand-mark"></span>Zentho</div>
    <article class="article">
      <h1>HOW ZENTHO DRIVES ADOPTION OF PREDICTIVE MAINTENANCE WITH MACHINE LEARNING</h1>
      <p>Predictive maintenance, or the practice of using data to anticipate equipment failures, has become a tool that delivers meaningful time and cost savings for a wide range of businesses. With an ability to reduce breakdowns by an average of <strong>70% and lower maintenance costs by an average of 25%,</strong> predictive maintenance is no longer an advanced R&amp;D initiative considered only by early adopters. It is delivering real results for assets used in manufacturing, construction, industrial printing, oil and gas exploration, healthcare, defense and more.</p>
      <p>At Zentho, we continue to develop machine learning tools that can bring predictive maintenance capabilities to businesses of all sizes dedicated to improving their operations, even those with modest budgets or</p>
      <p class="pull-quote">With an ability to reduce breakdowns by an average of 70% &amp; lower maintenance costs by an average of 25%, predictive maintenance is no longer an advanced R&amp;D initiative considered only by early adopters.</p>
      <p>limited technical capabilities. Our solutions have also helped department leaders be recognized for bringing a new and valuable analytics-based practice into the company.</p>
      <p>As the COVID-19 pandemic places new challenges on businesses of all types, those that adopt this valuable tool now will be better equipped to hit the ground running when global health and economic conditions improve.</p>
    </article>
    <footer class="page-footer">
      <span>Copyright © 2020 • Northwind Labs, Inc</span>
      <span><span class="site">ZENTHO.AI</span><span class="num">01</span></span>
    </footer>
  </section>
  <div class="page-label inner-label">PAGE 1</div>

  <section class="page back">
    <svg class="bands" width="334" height="473" viewBox="0 0 334 473" aria-hidden="true">
      <polygon points="180,0 334,0 334,150 100,473 0,473 0,430" fill="#dcdaf3" opacity=".6"/>
      <polygon points="0,0 60,0 334,330 334,473 230,473 0,150" fill="#d9efe3" opacity=".6"/>
    </svg>
    <div class="contact">
      <div class="brand">Zentho</div>
      <h2>CONTACT US</h2>
      <p class="about">We are a team of developers and data scientists from leading machine learning companies like Omnivelt, Brackwyn and Tarsolen, working behind the scenes to deliver exceptional models and experiences.</p>
      <p class="details">+1 (555) 014-2290 | hello@zentho.ai | https://zentho.ai/</p>
      <p class="copyright">Copyright © 2020 • Northwind Labs, Inc</p>
    </div>
  </section>
  <div class="page-label back-label">BACK</div>

</body>
</html>
```